Corvane Networks web design

Corvane is an Internet Service Provider bringing high-speed service to homes and businesses. Our principal market target is rural areas of West Michigan, but we intend to expand rapidly. We need a website to market our services, facilitate online ordering, customer support and communicate with our customers.

I will upload a draft outline of the content we hope to include in the website.

We compete directly with Halberd Communications, Lumetra, Dravix and Kelwick communications to bring Internet service to homes and businesses in our coverage area.

Our primary values include:

1. Unlike our competitors, we do not require long term contractors or service bundles; There are no termination fees, for example. All services are sold on a recurring 1-month agreement term.
2. Unlike other wireless (mobile) providers, we do not limit downloads or uploads with bit/byte buckets
3. We provide service to areas ignored by the larger carriers - Rural areas in Michigan that lack options for broadband are prime targets for Corvane to cover.
4. Unlike other wireless ISP's, we utilize licensed FCC spectrum. We do not use unlicensed/free frequencies, providing us an advantage for reliability and stability.
Updates

So many wonderful designs, thank you very much for all your hard work. We are evaluating all our favorite designs and plan to make a selection in the next 2 days. I will be in touch with you to request revisions if necessary or further refinements.  Thank you again for your efforts on this project.

Target Market(s)

Our target market is home Internet users. however, that does not mean that our users are "high tech" oriented - they are just normal mom's and pop's who buy Internet for home use. The site should be easy to navigate and communicate our message of speed, value, reliability and facilitate simple product ordering.

Industry/Entity Type

Internet

Requirements
Must have
• Our phone number should be prominently displayed 1-844-7NU-LINK
• Our logo is uploaded in the attachments.
• Design for desktop and mobile devices.
Nice to have
• The most modern of web design trends. Such as a design that facilitates parallax scrolling effects rather than lots of individual pages.
• Stock artwork communicating our values of speed and reliability.

```html
<!DOCTYPE html>
<html lang="en">
<head>
<meta charset="utf-8">
<title>Corvane Networks – West Michigan's Best Internet Service</title>
<link href="https://fonts.googleapis.com/css2?family=Lato:ital,wght@0,300;0,400;0,700;0,900;1,400&display=swap" rel="stylesheet">
<style>
:root{
  --orange:#f47c12;
  --orange-light:#ff9a1f;
  --ink:#333333;
  --muted:#555555;
  --panel:#4a4a4a;
  --panel-line:#5c5c5c;
  --pale:#f5f5f5;
  --footer:#3d3d3d;
  --footer-deep:#333333;
  --footer-text:#c4c4c4;
  --white:#ffffff;
}
*{box-sizing:border-box;margin:0;padding:0}
html,body{width:907px;height:1200px;overflow:hidden;background:var(--white)}
body{font-family:'Lato',sans-serif;color:var(--ink);position:relative}
.abs{position:absolute}

/* header */
.site-header{left:0;top:0;width:907px;height:76px;background:var(--white)}
.brand{left:150px;top:22px;display:flex;align-items:center;gap:6px;color:var(--orange);font-weight:900;font-size:18px;letter-spacing:1px}
.brand-dot{width:10px;height:10px;border-radius:50%;background:var(--orange)}
.contact{right:154px;top:11px;display:flex;gap:10px;font-size:9px;font-weight:700;color:var(--ink);align-items:center}
.contact span{display:flex;align-items:center;gap:5px}
.main-nav{right:154px;top:47px;display:flex;font-size:9px;color:var(--muted)}
.main-nav a{color:inherit;text-decoration:none;padding:0 13px;border-left:1px solid #bbb;line-height:10px}
.main-nav a:first-child{border-left:none;color:var(--orange)}
.main-nav a:last-child{padding-right:0}

/* hero */
.hero{left:0;top:76px;width:907px;height:253px}
.hero-scene{width:100%;height:100%;background:linear-gradient(90deg,#6b4fa8 0%,#8a6a70 25%,#5d6b4c 45%,#8fa9c4 60%,#c7cbd4 78%,#2b3a55 100%)}
.hero-copy{left:162px;top:84px;color:var(--white);text-shadow:0 2px 4px rgba(0,0,0,.45)}
.hero-copy h1{font-size:40px;font-weight:900;line-height:1;letter-spacing:-1px}
.hero-copy h1 small{font-size:33px;font-weight:400}
.hero-copy .tagline{font-size:29px;font-weight:400;letter-spacing:-1.2px;line-height:1.15}
.hero-copy .region{font-size:14px;font-weight:700;color:var(--orange-light)}

/* features */
.features{left:0;top:329px;width:907px;height:205px;background:var(--panel);display:grid;grid-template-columns:350px 202px 355px;grid-template-rows:102px 103px}
.feature{border-right:1px solid var(--panel-line);border-bottom:1px solid var(--panel-line);display:flex;flex-direction:column;align-items:center;justify-content:flex-end;padding-bottom:10px;color:var(--white);font-size:12px;text-align:center;line-height:1.2}
.feature svg{margin-bottom:8px}
.feature:nth-child(3n){border-right:none}

/* values */
.values{left:0;top:534px;width:907px;height:212px;background:var(--pale)}
.values h2{font-size:20px;font-weight:400;color:var(--ink);margin-bottom:14px}
.value-col{top:26px}
.value-col.left{left:152px;width:240px}
.value-col.right{left:500px;width:245px}
.value-divider{left:439px;top:38px;width:0;height:146px;border-left:1px dashed #bbb}
.value-item{display:flex;gap:8px;font-size:8.3px;color:var(--muted);line-height:1.35;margin-bottom:10px;font-weight:400}
.bullet{flex:0 0 10px;height:10px;margin-top:2px}

/* social strip */
.feed-head{top:775px;height:23px;width:195px;background:linear-gradient(#3a3a3a,#111);border-radius:2px;color:var(--white);font-size:12.5px;display:flex;align-items:center;gap:8px;padding-left:9px}
.news{left:151px;top:806px;width:194px}
.news li{list-style:none;font-size:7.6px;line-height:1.35;color:var(--ink);padding:1px 0 6px;border-bottom:1px dashed #bbb;margin-bottom:6px}
.news li:last-child{border-bottom:none}
.tweet{left:358px;width:182px;display:flex;gap:14px;align-items:center}
.avatar{width:36px;height:36px;border-radius:50%;background:linear-gradient(#c98d6a,#7a5140);border:2px solid #fff;box-shadow:0 1px 3px rgba(0,0,0,.3);flex:0 0 36px}
.bubble{border:2px solid #eee;border-radius:6px;padding:6px 8px;font-size:6.6px;font-style:italic;line-height:1.3;color:var(--ink);width:126px}
.post{left:566px;width:190px;display:flex;gap:7px}
.post .avatar{border-radius:2px;width:37px;height:37px;flex:0 0 37px}
.post h4{font-size:8px;font-weight:700}
.post h4 span{font-weight:400;font-style:italic;font-size:6.6px;color:var(--muted);margin-left:4px}
.post .date{font-size:6.6px;font-style:italic;color:var(--orange)}
.post p{font-size:6.6px;line-height:1.3;color:var(--ink);margin-left:1px}

/* call band */
.call-band{left:0;top:970px;width:907px;height:57px;background:linear-gradient(var(--orange-light),var(--orange));color:var(--white);text-align:center;font-size:19.5px;font-weight:700;line-height:23px;padding-top:5px;letter-spacing:-.5px;text-shadow:0 1px 3px rgba(0,0,0,.35)}

/* footer */
.site-footer{left:0;top:1027px;width:907px;height:139px;background:var(--footer)}
.foot-col{top:20px;font-size:8.5px;color:var(--footer-text);line-height:15.2px;font-weight:400}
.foot-col h5{font-size:9.5px;font-weight:700;color:var(--white);letter-spacing:.4px;margin-bottom:3px}
.foot-sep{top:38px;height:72px;border-left:1px solid #555}
.foot-brand{left:624px;top:30px;color:#d8d8d8}
.foot-brand .name{font-size:16px;font-weight:900;letter-spacing:1px;color:#d8d8d8}
.foot-brand p{font-size:9.5px;font-weight:700;color:var(--white);line-height:1.3;margin-top:6px}
.legal{left:0;top:1166px;width:907px;height:34px;background:var(--footer-deep);color:var(--footer-text);font-size:8.5px}
.legal .copy{position:absolute;left:152px;top:12px}
.legal nav{position:absolute;right:153px;top:12px;display:flex}
.legal nav a{color:inherit;text-decoration:none;padding:0 14px;border-left:1px solid #666;line-height:10px}
.legal nav a:first-child{border-left:none}
.legal nav a:last-child{padding-right:0}
</style>
</head>
<body>

<header class="site-header abs">
  <div class="brand abs"><span class="brand-dot"></span>CORVANE NETWORKS</div>
  <div class="contact abs">
    <span><svg width="10" height="10" viewBox="0 0 24 24"><path fill="#f47c12" d="M6.6 10.8a15 15 0 0 0 6.6 6.6l2.2-2.2c.3-.3.7-.4 1-.2 1.1.4 2.3.6 3.6.6.6 0 1 .4 1 1V20c0 .6-.4 1-1 1A17 17 0 0 1 3 4c0-.6.4-1 1-1h3.5c.6 0 1 .4 1 1 0 1.3.2 2.5.6 3.6.1.3 0 .7-.2 1z"/></svg>1-844-7NU-LINK</span>
    <span><svg width="12" height="10" viewBox="0 0 24 20"><circle cx="9" cy="6" r="5" fill="#f47c12"/><path fill="#f47c12" d="M0 20c0-5 4-8 9-8s9 3 9 8z"/></svg>517-555-0142</span>
  </div>
  <nav class="main-nav abs"><a href="#">Home</a><a href="#">Service Plans</a><a href="#">Coverage Map</a><a href="#">About Us</a></nav>
</header>

<section class="hero abs">
  <div class="hero-scene" role="img" aria-label="Excited man holding a laptop in front of a glowing speedometer over a blurred city background"></div>
  <div class="hero-copy abs">
    <h1>FASTER <small>SPEED,</small></h1>
    <div class="tagline">No Limits, More Value</div>
    <div class="region">West Michigan’s Best Internet Service</div>
  </div>
</section>

<section class="features abs">
  <div class="feature">
    <svg width="44" height="54" viewBox="0 0 44 54"><path fill="#fff" d="M12 32l-6 20 8-4 6 6 4-16zM32 32l6 20-8-4-6 6-4-16z"/><circle cx="22" cy="22" r="20" fill="#fff"/><circle cx="22" cy="22" r="14" fill="#f47c12"/><path d="M15 22l5 5 9-10" stroke="#4a4a4a" stroke-width="3" fill="none"/></svg>
    100% Satisfaction Guaranteed</div>
  <div class="feature">
    <svg width="34" height="54" viewBox="0 0 34 54"><text x="17" y="46" font-family="Lato,sans-serif" font-weight="900" font-size="52" fill="#fff" text-anchor="middle">$</text></svg>
    Honest Pricing, No Hidden Fees</div>
  <div class="feature">
    <svg width="46" height="54" viewBox="0 0 46 54"><path d="M3 2h26l10 10v36H3z" fill="none" stroke="#fff" stroke-width="3"/><path d="M9 14h18M9 20h24M9 26h24M9 32h16" stroke="#fff" stroke-width="2"/><circle cx="37" cy="45" r="7" fill="#fff"/><path d="M34 42l6 6M40 42l-6 6" stroke="#4a4a4a" stroke-width="2"/></svg>
    No Long Term Contracts</div>
  <div class="feature">
    <svg width="54" height="44" viewBox="0 0 54 44"><path d="M22 6l8 8M40 4l-8 10" stroke="#fff" stroke-width="3"/><rect x="12" y="14" width="40" height="28" rx="3" fill="none" stroke="#fff" stroke-width="3"/><rect x="17" y="19" width="22" height="18" fill="#fff"/><circle cx="46" cy="22" r="2" fill="#fff"/><path d="M2 42c0-8 4-12 10-12s10 4 10 12z" fill="#f47c12"/><circle cx="12" cy="37" r="3" fill="#4a4a4a"/></svg>
    No Phone Line or Cable TV required</div>
  <div class="feature">
    <svg width="50" height="44" viewBox="0 0 50 44"><path d="M2 2v40h46" stroke="#fff" stroke-width="3" fill="none"/><rect x="9" y="28" width="6" height="12" fill="#fff"/><rect x="18" y="22" width="6" height="18" fill="#fff"/><rect x="27" y="26" width="6" height="14" fill="#fff"/><rect x="36" y="16" width="6" height="24" fill="#fff"/><path d="M8 22l10-10 8 6 16-14" stroke="#f47c12" stroke-width="3" fill="none"/></svg>
    Fast, Superior Performance</div>
  <div class="feature">
    <svg width="50" height="40" viewBox="0 0 50 40"><path d="M3 13a32 32 0 0 1 44 0M10 20a22 22 0 0 1 30 0M17 27a12 12 0 0 1 16 0" stroke="#fff" stroke-width="4" fill="none" stroke-linecap="round"/><circle cx="25" cy="35" r="4" fill="#fff"/></svg>
    Interference-Free FCC Licensed<br>4G Coverage</div>
</section>

<section class="values abs">
  <div class="value-col left abs">
    <h2>Why Corvane?</h2>
    <div class="value-item"><svg class="bullet" viewBox="0 0 10 10"><circle cx="5" cy="5" r="5" fill="#f47c12"/></svg><p>No Download Limits! Corvane doesn’t charge you more when you use more</p></div>
    <div class="value-item"><svg class="bullet" viewBox="0 0 10 10"><circle cx="5" cy="5" r="5" fill="#f47c12"/></svg><p>No Cancellation Fees! All services are sold on 1-month terms, there are no contract minimums and never a cancellation fee.</p></div>
    <div class="value-item"><svg class="bullet" viewBox="0 0 10 10"><circle cx="5" cy="5" r="5" fill="#f47c12"/></svg><p>FCC Licensed reliability. Corvane 4G utilizes the latest wireless technologies using FCC licensed frequencies. Unlike other West Michigan ISP’s, our signals never fade. Enjoy stable and reliable Internet service.</p></div>
  </div>
  <div class="value-divider abs"></div>
  <div class="value-col right abs">
    <h2>Buy Local</h2>
    <div class="value-item"><svg class="bullet" viewBox="0 0 10 10"><circle cx="5" cy="5" r="5" fill="#f47c12"/></svg><p>Corvane is Local! We’re a locally owned and operated business. All of our staff live and work in Michigan. We in invest in our local community because we live it- just like you!</p></div>
    <div class="value-item"><svg class="bullet" viewBox="0 0 10 10"><circle cx="5" cy="5" r="5" fill="#f47c12"/></svg><p>Best Value, Best for You! Unlike cable and phone companies, we don’t require you to buy everything from us. We offer the best value Internet service, and only what you want, no “bundles” required.</p></div>
  </div>
</section>

<div class="feed-head abs" style="left:151px"><svg width="14" height="12" viewBox="0 0 14 12"><rect x="1" y="1" width="12" height="8" fill="none" stroke="#fff" stroke-width="1.5"/><path d="M3 4h8M3 6h6M3 9l-1 3 4-3" stroke="#fff" stroke-width="1"/></svg>Latest News Headlines</div>
<div class="feed-head abs" style="left:356px"><svg width="13" height="12" viewBox="0 0 13 12"><path d="M1 3l5 4 6-6" stroke="#fff" stroke-width="2" fill="none"/><path d="M1 9h11" stroke="#fff" stroke-width="1.5"/></svg>Latest Tweets</div>
<div class="feed-head abs" style="left:561px"><svg width="12" height="12" viewBox="0 0 12 12"><circle cx="2.5" cy="9.5" r="1.8" fill="#fff"/><path d="M1 5a6 6 0 0 1 6 6M1 1a10 10 0 0 1 10 10" stroke="#fff" stroke-width="1.6" fill="none"/></svg>Blog Posts</div>

<ul class="news abs">
  <li>Veridane <b>Demonstrates Advanced</b> Multiscreen Video at CTB Expo 2014</li>
  <li>Veridane Video Processing Selected by Northline One for Alpine Cup 2014 Coverage</li>
  <li>Veridane Streams 4K Content for <b>Multiple Screens</b> at TechShow 2014</li>
  <li>Veridane Debuts <b>Full Frame Rate Live</b> 4K HEVC Video Processing</li>
</ul>

<div class="tweet abs" style="top:812px"><div class="avatar" role="img" aria-label="Follower profile photo"></div><div class="bubble">Lorem ipsum dolor sit amet, consectetuer adipiscing elit, diam nonummy nibh euismod ti unt ut laoreet dolore.</div></div>
<div class="tweet abs" style="top:877px"><div class="avatar" role="img" aria-label="Follower profile photo" style="background:linear-gradient(#d9a07a,#3a2a22)"></div><div class="bubble">Lorem ipsum dolor sit amet, consectetuer adipiscing elit, diam nonummy nibh euismod ti unt ut laoreet dolore.</div></div>

<div class="post abs" style="top:815px"><div class="avatar" role="img" aria-label="Author profile photo" style="background:linear-gradient(#8a6a4a,#3b2c22)"></div><div><h4>Dana Whitfield<span>@DanaWhitfield</span></h4><div class="date">27-01-2014 On Monday</div><p>Consectetuer adipiscing elit, diam nonummy nibh euismod ti unt ut laoreet dolore.</p></div></div>
<div class="post abs" style="top:882px"><div class="avatar" role="img" aria-label="Author profile photo" style="background:linear-gradient(#7a8a6a,#5a3e2e)"></div><div><h4>Dana Whitfield<span>@DanaWhitfield</span></h4><div class="date">27-01-2014 On Monday</div><p>Consectetuer adipiscing elit, diam nonummy nibh euismod ti unt ut laoreet dolore.</p></div></div>

<div class="call-band abs">Call today to place an order or reach customer support<br>844-7NU-LINK Local number 517-555-0142</div>

<footer class="site-footer abs">
  <div class="foot-col abs" style="left:151px"><h5>NAVIGATION</h5>Service Plans<br>Coverage Map<br>Whois Corvane<br>Company Blog<br>Customer Support<br>Account Management</div>
  <div class="foot-sep abs" style="left:272px"></div>
  <div class="foot-col abs" style="left:315px"><h5>HELP</h5>Support Staff Hours<br>Weekdays 7am to 10pm<br>Weekends 8am to 5pm<br>Holiday scheduling varies</div>
  <div class="foot-sep abs" style="left:447px"></div>
  <div class="foot-col abs" style="left:485px;line-height:11px"><h5 style="margin-bottom:7px">ADDRESS</h5>Corvane Networks, LLC<br>1180 Harbor Lane<br>Cedar Hollow, MI 49990</div>
  <div class="foot-sep abs" style="left:595px"></div>
  <div class="foot-brand abs"><div class="name">CORVANE NETWORKS</div><p>Proud to live and work in<br>Michigan!</p></div>
</footer>

<div class="legal abs">
  <span class="copy">Copyright © 2012. Corvane Website Outline</span>
  <nav><a href="#">Home</a><a href="#">Service Plans</a><a href="#">Coverage Map</a><a href="#">About Us</a></nav>
</div>

</body>
</html>
```